wine bottle label design

My girlfriend and I are getting married. We are sending out invitations, in a wine bottle. For that we need a label on the bottle.
Our names are Marlene & Henrik. We would like the C and K to somehow play a bigger part in the logo.
Also maybe with an Illustration (best if made as a drawing resembling the church we are getting married in) https://www.sangfolket.dk/index.php/kalender/83-uncategorised/148-gospelgudstjeneste-i-tarnholm-kirke.html

Logo Text

Bryllup den 27 april 2019, kl. 14:00 i Tarnholm Kirke

Font styles to use
Decorative

```html
<!DOCTYPE html>
<html lang="da">
<head>
<meta charset="utf-8">
<title>Marlene &amp; Henrik – vinetiket</title>
<link rel="stylesheet" href="https://fonts.googleapis.com/css2?family=Great+Vibes&family=Mystery+Quest&display=swap">
<style>
  :root {
    --paper: #ffffff;
    --backdrop: #ecebe8;
    --frame: #d2501c;
    --name-start: #c8331a;
    --name-end: #ec7a22;
    --divider: #c9452a;
    --caption-fill: #ffffff;
    --caption-stroke: #3c3c3c;
    --wash-blue: rgba(170, 190, 225, 0.75);
    --wash-yellow: rgba(233, 200, 90, 0.8);
    --wash-green: rgba(170, 178, 80, 0.75);
    --wash-roof: rgba(205, 90, 60, 0.7);
  }
  * { margin: 0; padding: 0; box-sizing: border-box; }
  html, body {
    width: 1200px;
    height: 1200px;
    overflow: hidden;
    background: var(--backdrop);
  }
  .label {
    position: relative;
    width: 1200px;
    height: 1200px;
    background: var(--paper);
  }
  .label__frame {
    position: absolute;
    inset: 26px;
    border: 7px solid var(--frame);
    pointer-events: none;
  }
  .label__church {
    position: absolute;
    left: 50px;
    top: 300px;
    width: 980px;
    height: 800px;
    background:
      radial-gradient(ellipse 180px 230px at 300px 230px, var(--wash-blue), transparent),
      radial-gradient(ellipse 260px 150px at 460px 400px, var(--wash-roof), transparent),
      radial-gradient(ellipse 340px 200px at 420px 470px, var(--wash-yellow), transparent),
      radial-gradient(ellipse 440px 200px at 520px 580px, var(--wash-green), transparent);
    -webkit-mask-image: radial-gradient(ellipse 50% 50% at 50% 50%, #000 55%, transparent 100%);
    mask-image: radial-gradient(ellipse 50% 50% at 50% 50%, #000 55%, transparent 100%);
  }
  .label__names {
    font-family: "Great Vibes", cursive;
    font-weight: 400;
    line-height: 1;
  }
  .label__bride {
    position: absolute;
    left: 70px;
    top: 45px;
    font-size: 222px;
    white-space: nowrap;
    color: var(--name-start);
  }
  .label__groom {
    position: absolute;
    left: 510px;
    top: 270px;
    font-size: 210px;
    white-space: nowrap;
    color: var(--name-end);
  }
  .label__divider {
    position: absolute;
    left: 550px;
    top: 533px;
    width: 510px;
    height: 24px;
  }
  .label__details {
    position: absolute;
    right: 82px;
    top: 935px;
    text-align: right;
    font-family: "Mystery Quest", cursive;
    font-size: 80px;
    line-height: 1.18;
    color: var(--caption-fill);
    -webkit-text-stroke: 5px var(--caption-stroke);
    paint-order: stroke fill;
    text-shadow: 0 3px 6px rgba(0, 0, 0, 0.45);
    white-space: nowrap;
  }
</style>
</head>
<body>
  <main class="label">
    <div class="label__church" role="img" aria-label="Akvarel af Tarnholm Kirke med gult tårn, rødt tag og grønne træer"></div>

    <h1 class="label__names">
      <span class="label__bride">Marlene &amp;</span>
      <span class="label__groom">Henrik</span>
    </h1>

    <svg class="label__divider" viewBox="0 0 510 24" aria-hidden="true">
      <line x1="0" y1="12" x2="510" y2="12" stroke="var(--divider)" stroke-width="3"/>
      <rect x="247" y="4" width="16" height="16" transform="rotate(45 255 12)" fill="var(--divider)"/>
    </svg>

    <p class="label__details">Bryllup den 27 april 2019, kl.<br>14:00 i Tarnholm Kirke</p>

    <div class="label__frame"></div>
  </main>
</body>
</html>
```